Business Card for By Karel Voss

Looking to have a business card designed for my lifestyle and fitness company. My company offers personal training, online programming and nutrition advice based out of London, United Kingdom.

I'd like to see modern, sleek designs, focusing on black, matte black or matte grey. Design doesn't need to be overly descriptive as this will also be used as a personal business card. I've included my logo.

Please note that my company is no longer called "Fitness by Karel Voss" but instead "By Karel Voss", this is because of my other ventures. Therefore please don't use the "fitness by karel voss" text.

information about my company can be found at www.bykarelvoss.com

Company is also based out of London (United Kingdom) & Sydney (Australia) this could be reflected on the card.

Industry/Entity Type

Business

Contact Information for Business Card

Karel Voss
+44 7382 615027
karel@bykarelvoss.com
www.bykarelvoss.com

Font styles to use
Sans Serif

Requirements
Must have
• All contact details and inclusion of my logo.

```html
<!DOCTYPE html>
<html lang="en">
<head>
<meta charset="utf-8">
<title>By Karel Voss — Business Card</title>
<link rel="stylesheet" href="https://fonts.googleapis.com/css2?family=Roboto:wght@400;700&display=swap">
<style>
  :root {
    --backdrop: #d9d9d9;
    --card-black: #1c1a1b;
    --pattern-black: #242223;
    --card-white: #f3f3f3;
    --ink: #1e1e1e;
    --ink-soft: #3a3a3a;
    --paper-text: #ffffff;
  }
  * { margin: 0; padding: 0; box-sizing: border-box; }
  html, body {
    width: 1200px; height: 899px; overflow: hidden;
    background: var(--backdrop);
    font-family: "Roboto", Arial, sans-serif;
  }
  .canvas { position: relative; width: 1200px; height: 899px; }

  .card {
    position: absolute;
    width: 620px; height: 354px;
    overflow: hidden;
    box-shadow: 0 10px 24px rgba(0,0,0,0.18);
  }
  .card--back { left: 130px; top: 70px; background: var(--card-black); }
  .card--front { left: 450px; top: 470px; background: var(--card-white); display: flex; }

  .pattern {
    position: absolute; inset: 0;
    background: radial-gradient(circle at 50% 50%, var(--pattern-black), var(--card-black) 80%);
  }

  .brand {
    position: relative;
    display: flex; flex-direction: column; align-items: center; justify-content: center;
    height: 100%;
    color: var(--paper-text);
  }
  .brand__dot {
    width: 70px; height: 70px; border-radius: 50%;
    background: var(--paper-text);
    margin-bottom: 22px;
  }
  .brand__name {
    font-weight: 700; font-size: 34px; letter-spacing: 3px; text-transform: uppercase;
  }

  .front__info { position: relative; width: 53%; height: 100%; }
  .front__brand { position: relative; width: 47%; height: 100%; background: var(--card-black); }
  .front__brand .brand { justify-content: flex-start; padding-top: 34px; }
  .front__brand .brand__dot { width: 46px; height: 46px; margin-bottom: 14px; }
  .front__brand .brand__name { font-size: 18px; letter-spacing: 2px; }

  .accent-bar {
    position: absolute; left: 22px; top: 70px;
    width: 22px; height: 54px; background: var(--card-black);
  }
  .holder-name {
    position: absolute; left: 64px; top: 84px;
    font-weight: 700; font-size: 23px; color: var(--ink); text-transform: uppercase;
  }
  .contacts {
    position: absolute; left: 86px; top: 188px;
    list-style: none;
  }
  .contacts li {
    display: flex; align-items: center; gap: 14px;
    height: 42px;
    font-size: 16px; color: var(--ink-soft);
  }
  .contacts svg { width: 28px; height: 28px; flex: none; }
</style>
</head>
<body>
<main class="canvas">

  <section class="card card--back" aria-label="Card back">
    <div class="pattern" role="img" aria-label="Subtle concentric circle pattern on black"></div>
    <div class="brand">
      <span class="brand__dot"></span>
      <span class="brand__name">By Karel Voss</span>
    </div>
  </section>

  <section class="card card--front" aria-label="Card front">
    <div class="front__info">
      <span class="accent-bar"></span>
      <h1 class="holder-name">Karel Voss</h1>
      <ul class="contacts">
        <li>
          <svg viewBox="0 0 28 28" aria-hidden="true"><circle cx="14" cy="14" r="12.5" fill="none" stroke="#1e1e1e" stroke-width="1.6"/><path d="M10 8.5c-.8.3-1.5 1.2-1.3 2.6.5 3.4 4.4 7.8 8 8.4 1.3.2 2.3-.5 2.6-1.3l-2.2-1.9-1.5 1c-1.7-.7-3.3-2.3-4-4l1-1.5z" fill="#1e1e1e"/></svg>
          +44 7382 615027
        </li>
        <li>
          <svg viewBox="0 0 28 28" aria-hidden="true"><circle cx="14" cy="14" r="12.5" fill="none" stroke="#1e1e1e" stroke-width="1.6"/><rect x="7.5" y="9.5" width="13" height="9" fill="none" stroke="#1e1e1e" stroke-width="1.5"/><path d="M7.5 9.5l6.5 5 6.5-5" fill="none" stroke="#1e1e1e" stroke-width="1.5"/></svg>
          karel@bykarelvoss.com
        </li>
        <li>
          <svg viewBox="0 0 28 28" aria-hidden="true"><circle cx="14" cy="14" r="12.5" fill="none" stroke="#1e1e1e" stroke-width="1.6"/><circle cx="14" cy="14" r="6.5" fill="none" stroke="#1e1e1e" stroke-width="1.3"/><ellipse cx="14" cy="14" rx="3" ry="6.5" fill="none" stroke="#1e1e1e" stroke-width="1.2"/><path d="M7.5 14h13M8.5 10.8h11M8.5 17.2h11" stroke="#1e1e1e" stroke-width="1.1"/></svg>
          www.bykarelvoss.com
        </li>
      </ul>
    </div>
    <div class="front__brand">
      <div class="pattern" role="img" aria-label="Subtle concentric circle pattern on black"></div>
      <div class="brand">
        <span class="brand__dot"></span>
        <span class="brand__name">By Karel Voss</span>
      </div>
    </div>
  </section>

</main>
</body>
</html>
```